Business Card Design Project - Tall Maple

We are looking for a new business card design. Our company name is Tall Maple Communication Solutions. Our primary function is to provide our clients with communication solutions. These solutions include commercial phone systems and T1 and Fiber Internet lines. Another major part of the business is cabling new buildings with CAT5 cable for both data and phone.

Industry/Entity Type

Communication

Requirements
Must have
• The cards need to be two sided and have some bleeding edge color.
Nice to have
• We are going to upload our current logo BUT we are not married to this logo. If you want to incorporate a re-designed logo with the new business card - please feel free to do so. We are looking for a new bold look that is very colorful yet professional.

```html
<!DOCTYPE html>
<html lang="en">
<head>
<meta charset="utf-8">
<title>Tall Maple Communication Solutions – Business Cards</title>
<link rel="stylesheet" href="https://fonts.googleapis.com/css2?family=PT+Sans:wght@400;700&display=swap">
<style>
  :root {
    --backdrop: #1d1d1f;
    --navy: #2e3192;
    --royal: #2b2f8f;
    --sky: #1b93d1;
    --cyan: #3cc3e6;
    --white: #ffffff;
    --mark-light: #eeeeee;
    --mark-mid: #c9c9c9;
  }
  * { box-sizing: border-box; margin: 0; padding: 0; }
  html, body { width: 1200px; height: 709px; overflow: hidden; }
  body {
    background: var(--backdrop);
    font-family: "PT Sans", Arial, sans-serif;
    position: relative;
  }
  .card {
    position: absolute;
    width: 520px;
    height: 298px;
    border-radius: 14px;
    overflow: hidden;
    background: var(--white);
  }
  .card--back  { left: 35px;  top: 47px;
    background: radial-gradient(ellipse 60% 70% at 50% 45%, var(--sky) 0%, #2566b8 45%, var(--royal) 100%); }
  .card--front { left: 625px; top: 47px; }
  .card--alt   { left: 35px;  top: 368px; height: 297px; }
  .card--front-b { left: 625px; top: 372px; }

  .wave { position: absolute; left: 0; top: 0; width: 520px; height: 298px; }

  .brand { position: absolute; text-align: center; color: var(--navy); font-weight: 700; }
  .brand__dot { display: block; margin: 0 auto; border-radius: 50%;
    background: radial-gradient(circle at 40% 35%, var(--mark-light), var(--mark-mid)); }
  .card--back .brand__dot { background: radial-gradient(circle at 40% 35%, var(--cyan), var(--sky)); }
  .brand__name { display: block; line-height: 1; white-space: nowrap; }
  .brand__tag  { display: block; line-height: 1.1; white-space: nowrap; }

  .symbol-space {
    position: absolute; left: 20px; top: 27px; width: 250px; height: 250px; border-radius: 50%;
    background: radial-gradient(circle at 45% 40%, #fafafa 0%, #e6e6e6 70%, #d4d4d4 100%);
  }

  .person { position: absolute; color: var(--navy); white-space: nowrap; }
  .person--top { right: 18px; top: 30px; color: var(--white); font-size: 17px; }
  .person--mid { left: 326px; top: 171px; font-weight: 700; font-size: 14px; }

  .contact { position: absolute; font-size: 11px; line-height: 14.5px; color: var(--navy); white-space: nowrap; }
  .contact--address { left: 243px; }
  .contact--phones  { left: 387px; padding-left: 12px; border-left: 2px solid var(--navy); }
</style>
</head>
<body>

  <!-- Back side -->
  <section class="card card--back">
    <div class="brand" style="left:0; width:520px; top:58px;">
      <span class="brand__dot" style="width:108px; height:108px;"></span>
      <span class="brand__name" style="font-size:30px; margin-top:16px;">Tall Maple</span>
      <span class="brand__tag" style="font-size:15px; margin-top:4px;">Communication Solutions</span>
    </div>
  </section>

  <!-- Front side A -->
  <section class="card card--front">
    <svg class="wave" viewBox="0 0 520 298" aria-hidden="true">
      <defs>
        <radialGradient id="bandGlowA" cx="0.5" cy="0" r="0.5">
          <stop offset="0" stop-color="#3cc3e6"/>
          <stop offset="0.55" stop-color="#2a6fbf"/>
          <stop offset="1" stop-color="#2e3192"/>
        </radialGradient>
      </defs>
      <rect width="520" height="150" fill="url(#bandGlowA)"/>
      <path d="M0 90 C100 62 300 66 520 150 V298 H0 Z" fill="#2e3192"/>
      <path d="M0 78 C40 66 90 54 160 50 C260 46 400 88 520 136" fill="none" stroke="#fff" stroke-width="2.5"/>
      <path d="M0 92 C100 66 300 72 520 152 V298 H0 Z" fill="#fff"/>
    </svg>
    <p class="person person--top">Dana Whitfield</p>
    <div class="brand" style="left:-12px; width:200px; top:75px;">
      <span class="brand__dot" style="width:66px; height:66px;"></span>
      <span class="brand__name" style="font-size:20px; margin-top:10px;">Tall Maple</span>
      <span class="brand__tag" style="font-size:10px; margin-top:3px;">Communication Solutions</span>
    </div>
    <p class="contact contact--address" style="top:204px;">1480 W Ridgeline Avenue,<br>Suite 300<br>Tucson, AZ 85701</p>
    <p class="contact contact--phones" style="top:204px;">Office: 555.210.4410<br>Cell: 555.318.2296<br>24/7: 800.555.0147<br>Fax: 800.555.0193</p>
  </section>

  <!-- Alternate back -->
  <section class="card card--alt">
    <div class="symbol-space" role="img" aria-label="Space for the large logo symbol"></div>
    <div class="brand" style="left:294px; width:200px; top:72px;">
      <span class="brand__dot" style="width:94px; height:94px;"></span>
      <span class="brand__name" style="font-size:27px; margin-top:12px;">Tall Maple</span>
      <span class="brand__tag" style="font-size:14px; margin-top:4px;">Communication Solutions</span>
    </div>
  </section>

  <!-- Front side B -->
  <section class="card card--front-b">
    <svg class="wave" viewBox="0 0 520 298" aria-hidden="true">
      <defs>
        <radialGradient id="bandGlowB" cx="0.25" cy="0" r="0.5">
          <stop offset="0" stop-color="#3cc3e6"/>
          <stop offset="0.55" stop-color="#2a6fbf"/>
          <stop offset="1" stop-color="#2e3192"/>
        </radialGradient>
      </defs>
      <rect width="520" height="150" fill="url(#bandGlowB)"/>
      <path d="M0 82 C100 56 300 62 520 146 V298 H0 Z" fill="#2e3192"/>
      <path d="M0 70 C40 58 90 48 160 45 C260 42 400 82 520 130" fill="none" stroke="#fff" stroke-width="2.5"/>
      <path d="M0 84 C100 58 300 66 520 148 V298 H0 Z" fill="#fff"/>
    </svg>
    <div class="brand" style="left:4px; width:200px; top:113px;">
      <span class="brand__dot" style="width:86px; height:86px;"></span>
      <span class="brand__name" style="font-size:26px; margin-top:14px;">Tall Maple</span>
      <span class="brand__tag" style="font-size:13px; margin-top:4px;">Communication Solutions</span>
    </div>
    <p class="person person--mid">Dana Whitfield</p>
    <p class="contact contact--address" style="top:203px;">1480 W Ridgeline Avenue,<br>Suite 300<br>Tucson, AZ 85701</p>
    <p class="contact contact--phones" style="top:203px;">Office: 555.210.4410<br>Cell: 555.318.2296<br>24/7: 800.555.0147<br>Fax: 800.555.0193</p>
  </section>

</body>
</html>
```